Homepage design change needed

We're looking for a designer to change the way our homepage looks according to the attached sketch along with the project brief below.
Existing website is: http://www.tallowmere.co.nz
Please download the sketched design from the link below. https://www.parcelvoxa.com/s/k3m9q2x7t4w1z8r/fwdwebsitedesignneeded2.zip
There are 4 images inside the above zip file. front1, 2 & 3 make up the homepage.
page2.jpg is a sketch of what we'd like instead of the current page http://www.tallowmere.co.nz/join-tallowmere.aspx
Requirements
Must have
- The design must keep the following elements the same as the existing website:
- colour scheme
- same width
- same rounded corners/soft edges
- rounded buttons
- the graphics look of the following video brought through into the illustrations http://www.tallowmere.co.nz/help/video.aspx
front1.jpg - there is an illustration (3 boxes with = success! written); please don't design an illustration, simply leave space for a graphic to be put in its place later.
front2 and 3.jpg are to be fully designed as sketched. (again please ignore the illustration with 3 boxes = success!)

```html
<!DOCTYPE html>
<html lang="en">
<head>
<meta charset="utf-8">
<title>quorrelby — The Place to Hire and be Hired</title>
<link href="https://fonts.googleapis.com/css2?family=Fira+Sans:wght@300;400;500&family=Fira+Sans+Condensed:wght@500;600&display=swap" rel="stylesheet">
<style>
  :root {
    --page-bg: #eeeeee;
    --white: #ffffff;
    --brand-blue: #1b8ff3;
    --nav-blue: #178cf6;
    --hero-blue: #0f78d8;
    --hero-deep: #0a63b9;
    --panel-dark: #0b5cab;
    --highlight: #3f9ff0;
    --bar-light: #3592e6;
    --link-blue: #1a5fb4;
    --success-blue: #1667bd;
    --grey-text: #555e68;
    --box-border: #dcdcdc;
  }
  * { margin: 0; padding: 0; box-sizing: border-box; }
  html, body { width: 1200px; height: 900px; overflow: hidden; }
  body { background: var(--page-bg); font-family: "Fira Sans", sans-serif; position: relative; }

  .site-header {
    position: absolute; left: 121px; top: 0; width: 960px; height: 118px;
    background: var(--white); border-radius: 0 0 6px 6px; overflow: hidden;
    box-shadow: 0 2px 4px rgba(0,0,0,.15);
  }
  .brand {
    position: absolute; left: 37px; top: 20px;
    font-family: "Fira Sans", sans-serif; font-weight: 400; font-size: 36px;
    color: var(--brand-blue); letter-spacing: -0.5px;
  }
  .utility-links { position: absolute; right: 36px; top: 59px; display: flex; font: bold 12px Arial, sans-serif; }
  .utility-links a { color: var(--link-blue); text-decoration: none; padding: 0 8px; border-right: 1px solid var(--link-blue); line-height: 13px; }
  .main-nav {
    position: absolute; left: 0; top: 81px; width: 100%; height: 37px;
    background: var(--nav-blue); display: flex; align-items: center; padding-left: 37px;
  }
  .main-nav a { color: var(--white); text-decoration: none; font-family: "Fira Sans", sans-serif; font-weight: 500; font-size: 15px; margin-right: 48px; }

  .hero {
    position: absolute; left: 121px; top: 127px; width: 960px; height: 553px;
    border-radius: 6px 6px 0 0; overflow: hidden;
    background: radial-gradient(ellipse at 40% 30%, #1887e6 0%, var(--hero-blue) 55%, var(--hero-deep) 100%);
    color: var(--white);
  }
  .hero-title { position: absolute; top: 14px; left: 162px; white-space: nowrap; font-weight: 300; font-size: 36px; letter-spacing: -0.5px; }
  .hero-title strong { font-family: "Fira Sans Condensed", sans-serif; font-weight: 600; font-size: 47px; background: var(--highlight); padding: 0 4px; letter-spacing: 0; }
  .hero-sub { position: absolute; top: 74px; left: 199px; white-space: nowrap; font-weight: 300; font-size: 24px; letter-spacing: -0.2px; }
  .hero-rule { position: absolute; top: 124px; left: 0; width: 100%; height: 1px; background: #0a5eae; }
  .divider { position: absolute; left: 473px; top: 125px; width: 14px; height: 320px; background: var(--panel-dark); }
  .or-badge {
    position: absolute; left: 444px; top: 430px; width: 70px; height: 70px; border-radius: 50%;
    background: var(--panel-dark); display: flex; align-items: center; justify-content: center;
    font-family: "Fira Sans Condensed", sans-serif; font-weight: 600; font-size: 26px;
  }
  .column { position: absolute; top: 150px; }
  .column.seeker { left: 50px; }
  .column.employer { left: 544px; }
  .column h2 { font-family: "Fira Sans Condensed", sans-serif; font-weight: 600; font-size: 28.5px; line-height: 32px; white-space: nowrap; }
  .column .heading-bar { height: 8px; background: var(--bar-light); margin-top: 4px; }
  .seeker .heading-bar { width: 257px; }
  .employer .heading-bar { width: 359px; }
  .benefits { list-style: none; margin-top: 20px; }
  .benefits li { position: relative; padding-left: 38px; font-size: 14px; line-height: 24px; margin-bottom: 16px; width: 340px; }
  .benefits svg { position: absolute; left: 0; top: 0; }
  .cta {
    position: absolute; top: 360px; height: 66px; border-radius: 6px; background: var(--panel-dark);
    display: flex; align-items: center; font-family: "Fira Sans Condensed", sans-serif; font-weight: 600; font-size: 28px;
    color: var(--white); text-decoration: none; white-space: nowrap;
  }
  .cta.create { left: 50px; width: 340px; padding-left: 25px; }
  .cta.search { left: 544px; width: 340px; padding-left: 44px; }
  .cta-icon { position: absolute; top: 9px; left: 314px; width: 49px; height: 49px; border-radius: 50%; background: var(--white); }
  .how-it-works { position: absolute; top: 505px; width: 100%; text-align: center; font-family: "Fira Sans Condensed", sans-serif; font-weight: 600; font-size: 27px; }

  .explainer { position: absolute; left: 121px; top: 680px; width: 960px; height: 220px; background: var(--white); border-left: 1px solid #cfd9e4; border-right: 1px solid #cfd9e4; }
  .step-box { position: absolute; top: 14px; width: 235px; height: 230px; border: 1px solid var(--box-border); border-radius: 5px; }
  .step-plus { position: absolute; top: 106px; width: 43px; height: 43px; border-radius: 50%; background: var(--brand-blue); }
  .success { position: absolute; left: 760px; top: 102px; white-space: nowrap; font-family: "Fira Sans Condensed", sans-serif; font-weight: 600; font-size: 40px; color: var(--success-blue); }
  .success .equals { color: var(--grey-text); font-size: 30px; margin-right: 6px; }
</style>
</head>
<body>
  <header class="site-header">
    <div class="brand">quorrelby.co.nz</div>
    <nav class="utility-links">
      <a href="#">Home</a><a href="#">Join / Sign In</a><a href="#">Contact Us</a>
    </nav>
    <nav class="main-nav">
      <a href="#">Search to Hire</a>
      <a href="#">I want to be hired</a>
      <a href="#">Employer Services</a>
      <a href="#">My Quorrelby</a>
    </nav>
  </header>

  <section class="hero">
    <h1 class="hero-title">The Place to <strong>Hire</strong> and be <strong>Hired</strong></h1>
    <p class="hero-sub">putting you in the driver's seat (where you belong)</p>
    <div class="hero-rule"></div>
    <div class="divider"></div>

    <div class="column seeker">
      <h2>I want to be hired .....</h2>
      <div class="heading-bar"></div>
      <ul class="benefits">
        <li><svg width="24" height="22" viewBox="0 0 24 22"><path d="M2 12 L9 19 L22 2" fill="none" stroke="#fff" stroke-width="4" stroke-linecap="round" stroke-linejoin="round"/></svg>Advertise yourself in your own words</li>
        <li><svg width="24" height="22" viewBox="0 0 24 22"><path d="M2 12 L9 19 L22 2" fill="none" stroke="#fff" stroke-width="4" stroke-linecap="round" stroke-linejoin="round"/></svg>Employers approach you directly</li>
        <li><svg width="24" height="22" viewBox="0 0 24 22"><path d="M2 12 L9 19 L22 2" fill="none" stroke="#fff" stroke-width="4" stroke-linecap="round" stroke-linejoin="round"/></svg>Accept Job Offers, create extra income on your own terms</li>
      </ul>
    </div>

    <div class="column employer">
      <h2>I want to hire someone .....</h2>
      <div class="heading-bar"></div>
      <ul class="benefits">
        <li><svg width="24" height="22" viewBox="0 0 24 22"><path d="M2 12 L9 19 L22 2" fill="none" stroke="#fff" stroke-width="4" stroke-linecap="round" stroke-linejoin="round"/></svg>Search profiles for free</li>
        <li><svg width="24" height="22" viewBox="0 0 24 22"><path d="M2 12 L9 19 L22 2" fill="none" stroke="#fff" stroke-width="4" stroke-linecap="round" stroke-linejoin="round"/></svg>Contact people directly for free</li>
        <li><svg width="24" height="22" viewBox="0 0 24 22"><path d="M2 12 L9 19 L22 2" fill="none" stroke="#fff" stroke-width="4" stroke-linecap="round" stroke-linejoin="round"/></svg>Immediate access to thousands of people</li>
      </ul>
    </div>

    <a class="cta create" href="#">create your profile now
      <svg class="cta-icon" viewBox="0 0 49 49"><circle cx="24.5" cy="24.5" r="24.5" fill="#fff"/><path d="M24.5 13 V36 M13 24.5 H36" stroke="#0b5cab" stroke-width="4"/></svg>
    </a>
    <a class="cta search" href="#">search a person now
      <svg class="cta-icon" viewBox="0 0 49 49"><circle cx="24.5" cy="24.5" r="24.5" fill="#fff"/><circle cx="27" cy="21" r="6.5" fill="none" stroke="#0b5cab" stroke-width="3"/><path d="M22 26 L14 34" stroke="#0b5cab" stroke-width="4" stroke-linecap="round"/></svg>
    </a>

    <div class="or-badge">or</div>
    <h2 class="how-it-works">See How Career Quorrel Works</h2>
  </section>

  <section class="explainer">
    <div class="step-box" style="left:15px"></div>
    <div class="step-box" style="left:265px"></div>
    <div class="step-box" style="left:515px"></div>
    <svg class="step-plus" style="left:237px" viewBox="0 0 43 43"><circle cx="21.5" cy="21.5" r="21.5" fill="#1b8ff3"/><path d="M21.5 13 V30 M13 21.5 H30" stroke="#fff" stroke-width="3.5"/></svg>
    <svg class="step-plus" style="left:486px" viewBox="0 0 43 43"><circle cx="21.5" cy="21.5" r="21.5" fill="#1b8ff3"/><path d="M21.5 13 V30 M13 21.5 H30" stroke="#fff" stroke-width="3.5"/></svg>
    <div class="success"><span class="equals">=</span>success !!!</div>
  </section>
</body>
</html>
```